Tomo Rasu bar restaurant japanese street food

Hello dear friends!

We are a Gyoza Bar, specializing in square sandwiches (made with Hokkaido bread) and gyoza dumplings.

Our interior is designed to look like a Japanese street, with many signboards, street signs, and urban elements. We will attach photos so you can capture the overall vibe and atmosphere.

Our kitchen concept is street food.

Today we have a task to develop a takeaway / delivery box for our food.

We truly love our product and want to give it a professional and distinctive presentation.

Custom packaging is an important part of our brand style.

We appreciate non-standard solutions, shapes, and sizes.

About our product
We are a Gyoza Bar, and we have several types of gyoza:

Beef

Pork

Chicken

Vegetable

Salmon & Shrimp

What we need
We need one universal box for all flavors, with flavor indicators that we can mark when assembling an order.

A standard portion contains 6 dumplings.

Size of one dumpling:

Length: 7.5 cm

Height: 3.5 cm

Inside the box
The box must include:

An integrated sauce container

Diameter: 6 cm

Height: 3 cm

Shape: wider toward the top than the bottom

Chopsticks placed inside the box

Dividers between dumplings so they do not stick together

We imagine the box as a long rectangular shape.

Multiple portions
If an order includes several portions, the boxes should be able to connect or stack together.

For example:

stacking one box on top of another

small locking tabs or “ears” that allow the boxes to be connected together

You will see reference examples in the attachments.

Design
The design direction is up to you, as we like both:

minimalist concepts

more detailed / graphic designs

The most important thing is:
please do not make the logo too small, because it needs to remain clearly readable.

Final deliverable
The final result should be a packaging dieline (flat layout) that we can send directly to production without additional questions.

Thank you all for your attention and good luck!
If you have any questions, we will be happy to answer them.

P.S.

We also need a second box for other dishes with the following dimensions:

12.5 cm × 12.5 cm
Height: 7 cm

Target Market(s)

Please note that we are a high-quality street food brand. Packaging is part of our identity. We communicate through packaging

Requirements
Must have
• Chopsticks and a sauce container must be integrated into the packaging.

```html
<!DOCTYPE html>
<html lang="en">
<head>
<meta charset="utf-8">
<title>Tomo Rasu – Chicken Gyoza Box</title>
<link rel="stylesheet" href="https://fonts.googleapis.com/css2?family=Russo+One&family=Noto+Sans+JP:wght@900&display=swap">
<style>
  :root {
    --page: #ffffff;
    --box-pink: #ecd8d3;
    --brand-red: #d71f26;
    --cream: #efd9c4;
    --ink: #2a2a2a;
    --coral: #e05a5a;
    --ray-red: #e2504f;
    --sky: #5bc2e0;
    --mask-pink: #f1dcd9;
  }
  html, body {
    margin: 0;
    width: 1200px;
    height: 1200px;
    overflow: hidden;
    background: var(--page);
  }
  .box-front {
    position: absolute;
    left: 50px;
    top: 335px;
    width: 1100px;
    height: 530px;
    background: linear-gradient(90deg, #ebd6d1 0%, var(--box-pink) 50%, #ead3ce 100%);
    overflow: hidden;
  }
  .brand-block {
    position: absolute;
    left: 41px;
    top: 32px;
    width: 175px;
    height: 271px;
    background: var(--brand-red);
    display: flex;
    flex-direction: column;
    justify-content: flex-end;
    padding: 0 14px 12px;
    box-sizing: border-box;
  }
  .brand-name {
    font-family: "Russo One", sans-serif;
    font-size: 46px;
    line-height: 1.12;
    color: var(--cream);
    margin: 0;
    text-transform: uppercase;
  }
  .sun-rays {
    position: absolute;
    left: 0;
    top: 0;
    width: 1100px;
    height: 530px;
  }
  .sun-rays polygon { fill: var(--ray-red); }
  .sky-disc {
    position: absolute;
    left: 386px;
    top: 104px;
    width: 354px;
    height: 354px;
    border-radius: 50%;
    background: var(--sky);
  }
  .mascot-art {
    position: absolute;
    left: 349px;
    top: 103px;
    width: 354px;
    height: 335px;
    border-radius: 46% 46% 42% 42%;
    background: radial-gradient(ellipse at 55% 50%, var(--mask-pink) 0 55%, #f4eeee 80%, rgba(244,238,238,0) 100%);
  }
  .dish-kanji {
    position: absolute;
    left: 261px;
    top: 96px;
    font-family: "Noto Sans JP", sans-serif;
    font-weight: 900;
    font-size: 108px;
    line-height: 1.08;
    color: var(--ink);
    writing-mode: vertical-rl;
    margin: 0;
  }
  .flavour-badge {
    position: absolute;
    left: 686px;
    top: 108px;
    width: 168px;
    height: 168px;
    border-radius: 50%;
    background: var(--coral);
    border: 4px solid var(--ink);
    display: flex;
    align-items: center;
    justify-content: center;
  }
  .flavour-name {
    font-family: "Russo One", sans-serif;
    font-size: 33px;
    color: #ffffff;
    text-transform: uppercase;
    transform: skewX(-10deg) scaleX(0.9);
  }
  .portion {
    position: absolute;
    left: 731px;
    top: 325px;
    font-family: "Russo One", sans-serif;
    text-transform: uppercase;
    transform: skewX(-10deg);
    transform-origin: left top;
  }
  .portion-count {
    position: absolute;
    left: 0;
    top: 34px;
    font-size: 92px;
    line-height: 1;
    color: var(--brand-red);
  }
  .portion-label {
    position: absolute;
    left: 60px;
    top: 0;
    margin: 0;
    font-size: 56px;
    line-height: 58px;
    color: var(--ink);
    white-space: nowrap;
    transform: scaleX(0.68);
    transform-origin: left top;
  }
</style>
</head>
<body>
  <main class="box-front">
    <div class="brand-block">
      <p class="brand-name">Tomo<br>Rasu</p>
    </div>

    <svg class="sun-rays" viewBox="0 0 1100 530" aria-hidden="true">
      <polygon points="441,0 484,0 556,118 541,128"/>
      <polygon points="597,0 630,0 606,84 582,84"/>
      <polygon points="779,0 817,0 633,135 621,123"/>
    </svg>

    <div class="sky-disc"></div>

    <div class="mascot-art" role="img" aria-label="Illustration of a fox mask wrapped in white steam clouds"></div>

    <h1 class="dish-kanji">餃子</h1>

    <div class="flavour-badge">
      <span class="flavour-name">Chicken</span>
    </div>

    <div class="portion">
      <span class="portion-count">6</span>
      <p class="portion-label">Gyoza<br>Dumplings</p>
    </div>
  </main>
</body>
</html>
```